3 glossy INFOGRAPHIC SPLASH PAGES for website of video production / photography studio website

Hello. We need 3 designed infographic images to act as 'splash pages' on our work-in-progress website to offer detailed information to visitors.
1. MUDMAP
2. RATECARD
3. STUDIO FLOORPLAN

To view the website WIP - Go here: http://www.sitevault.com.au/pelbrook/

Regarding FILE SIZES:

The MUDMAP should sit in landscape with dimensions 2048px wide x 1536px high.

The RATECARD and STUDIO FLOORPLAN should be laid out in PORTRAIT with dimensions 1526px wide x 2048px high.

Regarding DESIGNS:

First is a 'MUD MAP' that details travel and parking directions for visitors to our studio,

Second is a floorplan of our studio space, and

Third is a Studio Hire Rate Card.

We want these images to utilise our new theme / branding / logos (attached) and ultimately these designs need to be easily read and understood.

Attached Files (may not be in order in brief, but here is my list):

Target Market(s)

potential studio hire customers (mainly producers)

Industry/Entity Type

Film Production

Font styles to use
Sans Serif
Other font styles liked:
• I have supplied branding fonts to be used as you see fit.

Colors
fbed22
00a990
0292cd
fece3e
f78f20
f37122

Requirements
Must have
• Supplied logos and branding theme / colours (see attached).
• Predominantly gold colour (specific gold supplied) as well as utilising colour theme (see attached)
Nice to have
• Would be nice if all three images have a continuity in their layout / design

```html
<!DOCTYPE html>
<html lang="en">
<head>
<meta charset="utf-8">
<title>Pelbrook Studio Hire Rates</title>
<link href="https://fonts.googleapis.com/css2?family=Carlito:wght@400;700&display=swap" rel="stylesheet">
<style>
:root{
  --bg:#121722;
  --panel:#3a3944;
  --gold:#c9a74a;
  --text:#ffffff;
}
*{margin:0;padding:0;box-sizing:border-box}
html,body{width:894px;height:1200px;overflow:hidden;background:var(--bg)}
body{font-family:"Carlito",Calibri,Arial,sans-serif;color:var(--text);font-size:14.6px;line-height:20px}
.page{position:relative;width:894px;height:1200px}
.title{position:absolute;top:48px;left:0;width:100%;text-align:center;color:var(--gold);font-weight:700;font-size:19px;line-height:26px}
.box{position:absolute;left:51px;width:796px;background:var(--panel);border:2px solid var(--gold);padding:4px 15px 8px 16px}
.box h2{color:var(--gold);font-size:14.8px;font-weight:700;text-align:center;line-height:20px}
.lbl{color:var(--gold);font-weight:700}
.gap{height:20px}
.ind{padding-left:65px}
.ind2{padding-left:70px}
p{margin:0}
.hire{top:95px;height:296px}
.viewing{top:405px;height:173px}
.extras{top:590px;height:148px}
.terms{top:750px;height:423px}
</style>
</head>
<body>
<div class="page">
  <div class="title">PELBROOK STUDIO HIRE RATES - effective 1st&nbsp; Jan 2016</div>

  <section class="box hire">
    <h2>Soundproof Studio Hire:</h2>
    <div class="gap"></div>
    <p><span class="lbl">BumpIn / Out:</span> $180 p/4hrs (available weekdays only)</p>
    <div class="gap"></div>
    <p><span class="lbl">Mon-Fri:</span> $350 p/half day (upto 5 hours*)</p>
    <p class="ind">$550 p/full day (upto 10 hours)</p>
    <p class="ind">$150 p/hr overtime (beyond 10 hours)</p>
    <div class="gap"></div>
    <p><span class="lbl">Saturday:</span> $450 p/half day (upto 5 hours*)</p>
    <p class="ind2">$650 p/full day (upto 10 hours)</p>
    <p class="ind2">$200 p/hr overtime (beyond 10 hours)</p>
    <div class="gap"></div>
    <p>*Any half day rental that exceeds 5 hours automatically becomes a full day hire..</p>
    <p>Video Studio Hire includes: 10 &amp; 15 amp power outlets, FBL Enabled ethernet &amp; Wi-fi, toilet.</p>
  </section>

  <section class="box viewing">
    <h2>Dedicated Client Viewing Area:<br>(to be used in conjunction with studio hire only)</h2>
    <div class="gap"></div>
    <p><span class="lbl">Mon-Fri:</span> $250 p/day</p>
    <p><span class="lbl">Saturday:</span> $300 p/day</p>
    <div class="gap"></div>
    <p>Client Viewing Area includes coffee machine, bottled water, fridge, 65” 4k viewing monitor, leather couch, boardroom table, additional bathroom &amp; toilet, FBL enabled ethernet &amp; wifi.</p>
  </section>

  <section class="box extras">
    <h2>Extras:</h2>
    <div class="gap"></div>
    <p><span class="lbl">Catering:</span> Contact us for healthy, fresh, locally sourced catering options. Gluten Free and vegetarian options also available.</p>
    <p><span class="lbl">Equipment:</span> Reference monitor, C-Stands and Lighting stands available on request for additional fee.</p>
    <p><span class="lbl">Opening hours:</span> For advanced Studio bookings, opening hours are 7am weekdays and 9am weekends.</p>
    <p>Earlier opening times can be arranged on request.</p>
  </section>

  <section class="box terms">
    <h2>Terms &amp; Conditions:</h2>
    <div class="gap"></div>
    <p><span class="lbl">Payment:</span> 14 day account terms applies to all verified account holders, otherwise payment must be made in full at end of usage (via cardlink).</p>
    <div class="gap"></div>
    <p><span class="lbl">Cancellation:</span> Cancellation fees apply to bookings cancelled less than 24 hours before agreed studio hire start time.</p>
    <div class="gap"></div>
    <p><span class="lbl">Damage Policy:</span> Pelbrook Studios understands that sometimes things happen, and general wear-and-tear is an unavoidable fact of life. However, if significant damage or breakages occur, the cost of repair or replacement will be placed solely onto the Hirer. We also expect our studio wall to be left in the same relative condition as it was found, and any significant damage will result ina replastering andrepainting fee of $350.</p>
    <div class="gap"></div>
    <p>At Pelbrook Studios, we endeavour to make your shooting experience run as smoothly as possible. We are here to listen to your requirements and assist you in any way, so feel free to contact us well before your shoot to see how we can help.</p>
    <div class="gap"></div>
    <p>Pelbrook Studios is also wellquipped with 24 hour CCTV and is fully alarmed.</p>
    <div class="gap"></div>
    <p>Unless otherwise indicated, all prices above are exclusive of GST.</p>
  </section>
</div>
</body>
</html>
```